Website redesign for job agency recruitment

Please refer to the attached document, “Harbor Work Portal Outline,” for comprehensive details regarding the scope, objectives, and requirements of this website redesign project.

For imagery you can use images from this website https://www.pixvaultmedia.com or any other you regularly use.

Target Market(s)

Jobseekers and Companies looking for general labour

Industry/Entity Type

Services: Oil, Gas and Mining, Administrative, Construction and Trades, Warehouse and Logistics and, Manufacturing.

Number of Pages Required

5+ page

Font styles to use
Serif
Other font styles liked:
• Inter, Open-Sans or similar.

Requirements
Must have
• The requirements highlighted in the Word document attached. The final design needs to be provided in Figma including all viewports (Desktop, mobiel and tablet)
Should not have
• Website we like as a reference: www.beltonworkforceinc.com, www.veltaworkforce.com, www.zplacer.com, www.brimwellworkforce.com, www.9tworkcrew.com, www.hiringonthemove.ca

```html
<!DOCTYPE html>
<html lang="en">
<head>
<meta charset="utf-8">
<title>Harbor Work Agency — Staffing Solutions</title>
<link rel="stylesheet" href="https://fonts.googleapis.com/css2?family=Outfit:wght@300;400;500;600;700;800&display=swap">
<style>
  :root {
    --navy: #0e2b6e;
    --blue: #0c3b9c;
    --blue-deep: #0a2a78;
    --yellow: #f5b914;
    --yellow-soft: #f7c637;
    --ink: #1d2433;
    --muted: #5b6272;
    --mist: #eef0f5;
    --white: #ffffff;
    --font: "Outfit", "Helvetica Neue", Arial, sans-serif;
  }
  * { margin: 0; padding: 0; box-sizing: border-box; }
  html, body { width: 1200px; height: 3700px; overflow: hidden; }
  body { position: relative; background: var(--white); font-family: var(--font); color: var(--ink); }
  .abs { position: absolute; }

  /* backdrop */
  .backdrop { position: absolute; left: 0; top: 0; width: 1200px; height: 3700px; }
  .hero-photo {
    position: absolute; left: 0; top: 0; width: 1200px; height: 860px;
    background:
      radial-gradient(circle at 830px 300px, rgba(255,214,120,.95) 0, rgba(236,160,60,.55) 110px, rgba(120,90,70,.2) 300px, transparent 420px),
      linear-gradient(100deg, #0c1a3c 0%, #1b2d52 35%, #4a5670 60%, #6b5a48 78%, #2a2a33 100%);
  }

  /* header */
  .brand { display: flex; align-items: center; gap: 8px; color: var(--white); font-weight: 700; white-space: nowrap; }
  .brand-dot { width: 14px; height: 14px; border-radius: 50%; background: var(--yellow); flex: none; }
  .site-header .brand { left: 93px; top: 40px; font-size: 19px; }
  .main-nav { left: 366px; top: 45px; display: flex; gap: 22px; font-size: 13.5px; color: var(--white); align-items: center; white-space: nowrap; }
  .main-nav svg { width: 16px; height: 16px; }
  .btn {
    display: inline-flex; align-items: center; justify-content: center;
    border-radius: 40px; font-weight: 600; text-transform: uppercase; font-size: 14px; white-space: nowrap;
  }
  .btn-yellow { background: var(--yellow); color: var(--white); }
  .btn-register { left: 941px; top: 34px; width: 165px; height: 42px; text-transform: none; font-size: 13.5px; }

  /* hero */
  .hero-title { left: 138px; top: 258px; font-size: 54px; line-height: 60px; font-weight: 700; color: var(--white); letter-spacing: -.5px; }
  .btn-candidates { left: 138px; top: 472px; width: 190px; height: 50px; }
  .btn-employers { left: 336px; top: 472px; width: 181px; height: 50px; background: rgba(255,255,255,.28); color: var(--white); }

  /* staffing */
  .section-title { font-size: 34px; font-weight: 700; color: var(--navy); text-align: center; width: 1200px; left: 0; letter-spacing: -.3px; }
  .solutions-title { top: 830px; }
  .node { width: 82px; height: 82px; border-radius: 50%; background: var(--white); box-shadow: 0 6px 18px rgba(14,43,110,.18); display: flex; align-items: center; justify-content: center; }
  .node-inner { width: 64px; height: 64px; border-radius: 50%; background: #e6ebf5; display: flex; align-items: center; justify-content: center; }
  .node-inner svg { width: 32px; height: 32px; }
  .node.is-active .node-inner { background: var(--yellow); }
  .node-label { font-size: 16px; font-weight: 500; color: var(--navy); white-space: nowrap; }
  .diagram-name { left: 450px; top: 978px; width: 300px; text-align: center; font-size: 78px; font-weight: 800; color: var(--blue-deep); letter-spacing: -1px; }
  .sector-title { left: 0; width: 1200px; top: 1190px; text-align: center; font-size: 16px; font-weight: 500; color: var(--navy); }
  .sector-text { left: 420px; width: 360px; top: 1222px; text-align: center; font-size: 12px; line-height: 19px; color: var(--muted); }
  .link-more { font-size: 12.5px; font-weight: 600; color: var(--yellow); }
  .sector-link { left: 0; width: 1200px; top: 1272px; text-align: center; }

  /* about */
  .about-photo { left: 141px; top: 1463px; width: 430px; height: 430px; border-radius: 50%; background: linear-gradient(135deg, #c9ccd4 0%, #8d9099 45%, #3f4450 100%); box-shadow: 0 14px 30px rgba(0,0,0,.12); }
  .about-title { left: 644px; top: 1530px; font-size: 34px; line-height: 38px; font-weight: 700; color: var(--navy); }
  .about-text { left: 644px; top: 1626px; width: 390px; font-size: 11.5px; line-height: 17.5px; color: var(--muted); }
  .about-text p + p { margin-top: 9px; }
  .btn-about { left: 644px; top: 1776px; width: 158px; height: 44px; font-size: 12.5px; }

  /* locations */
  .locations-title { top: 2088px; color: var(--white); }
  .location-card { top: 2158px; width: 301px; height: 339px; background: var(--white); border-radius: 30px; overflow: hidden; box-shadow: 0 10px 26px rgba(14,43,110,.12); }
  .location-photo { height: 230px; }
  .location-name { position: absolute; left: 42px; top: 258px; font-size: 17.5px; font-weight: 500; color: var(--blue); }
  .location-card .link-more { position: absolute; left: 42px; top: 287px; font-size: 12px; }

  /* testimonials */
  .testimonial-title { top: 2578px; line-height: 40px; font-size: 33px; }
  .quote-badge { left: 552px; top: 2687px; width: 95px; height: 94px; border-radius: 18px; background: var(--yellow); color: var(--blue); font-size: 110px; font-weight: 800; line-height: 150px; text-align: center; }
  .quote-ghost { left: 165px; top: 2720px; font-size: 240px; font-weight: 800; color: #f7ecd0; line-height: 1; opacity: .7; }
  .quote-text { left: 250px; width: 700px; top: 2808px; text-align: center; font-size: 17.5px; line-height: 26px; font-style: italic; font-weight: 300; color: #4a505e; }
  .stars { left: 0; width: 1200px; top: 2880px; display: flex; justify-content: center; gap: 6px; }
  .stars svg { width: 20px; height: 20px; }
  .quote-author { left: 0; width: 1200px; top: 2915px; text-align: center; font-size: 17px; color: #2c3140; }
  .dots { left: 582px; top: 2966px; display: flex; gap: 4px; }
  .dots span { width: 9px; height: 9px; border-radius: 2px; background: #cdd7ee; }
  .dots span:first-child { background: var(--blue); }

  /* cta */
  .cta { left: 96px; top: 3054px; width: 1008px; height: 230px; border-radius: 115px; border: 7px solid var(--white); background: linear-gradient(90deg, var(--yellow) 0%, var(--yellow-soft) 60%, #e9b52a 100%); box-shadow: 0 10px 24px rgba(0,0,0,.08); }
  .cta-name { left: 140px; top: 3150px; width: 230px; font-size: 30px; font-weight: 700; color: var(--navy); display: flex; align-items: center; gap: 10px; white-space: nowrap; }
  .cta-name .brand-dot { width: 18px; height: 18px; background: var(--white); }
  .cta-kicker { left: 400px; top: 3112px; font-size: 12px; font-weight: 600; color: var(--white); }
  .cta-heading { left: 400px; top: 3137px; font-size: 25px; line-height: 30px; font-weight: 700; color: var(--white); }
  .btn-apply { left: 868px; top: 3149px; width: 170px; height: 50px; background: var(--white); color: var(--navy); text-transform: none; font-size: 15px; }

  /* footer */
  .site-footer .brand { left: 170px; top: 3400px; font-size: 17px; }
  .footer-tagline { left: 170px; top: 3432px; font-size: 9.5px; color: #cfd8ee; font-style: italic; }
  .socials { left: 216px; top: 3516px; display: flex; gap: 11px; }
  .socials span { width: 31px; height: 31px; border-radius: 50%; background: rgba(255,255,255,.22); }
  .footer-col h4 { font-size: 19px; font-weight: 600; color: var(--white); margin-bottom: 18px; }
  .footer-col li { list-style: none; font-size: 11px; line-height: 20.7px; color: #dbe3f5; white-space: nowrap; }
  .footer-col p { font-size: 11px; color: #dbe3f5; white-space: nowrap; }
  .col-links { left: 407px; top: 3370px; }
  .col-contact { left: 586px; top: 3370px; }
  .col-news { left: 770px; top: 3370px; }
  .news-input { left: 772px; top: 3453px; width: 270px; height: 40px; border-radius: 20px; background: rgba(255,255,255,.14); color: #c9d3ec; font-size: 11px; padding: 13px 28px; }
  .btn-subscribe { left: 772px; top: 3503px; width: 270px; height: 42px; font-size: 11px; }
  .bottom-bar { left: 88px; top: 3627px; width: 1023px; height: 49px; border-radius: 25px; background: #0a2766; color: #dbe3f5; font-size: 11.5px; }
  .bottom-bar .copy { position: absolute; left: 0; width: 100%; top: 16px; text-align: center; }
  .bottom-bar .legal { position: absolute; right: 26px; top: 16px; }
  .chat-bubble { left: 1121px; top: 3611px; width: 80px; height: 80px; border-radius: 50%; background: var(--yellow); border: 5px solid var(--white); display: flex; align-items: center; justify-content: center; }
  .chat-bubble svg { width: 36px; height: 36px; }
</style>
</head>
<body>

<div class="hero-photo" role="img" aria-label="Looking up at a tall office skyscraper against a cloudy sky with golden sunlight"></div>

<svg class="backdrop" viewBox="0 0 1200 3700" aria-hidden="true">
  <defs>
    <linearGradient id="cityBlue" x1="0" y1="0" x2="0" y2="1">
      <stop offset="0" stop-color="#143f9e"/>
      <stop offset="1" stop-color="#0b3594"/>
    </linearGradient>
  </defs>
  <path d="M340,738 C560,690 820,690 980,722 C1090,745 1160,775 1200,792 V900 H340 Z" fill="#f5b914"/>
  <path d="M0,812 C220,748 440,722 640,724 L640,900 H0 Z" fill="#0c3b9c"/>
  <path d="M0,852 C200,785 430,743 650,742 C900,742 1100,790 1200,852 V900 H0 Z" fill="#ffffff"/>
  <path d="M0,1444 C300,1320 900,1320 1200,1444 V2110 H0 Z" fill="#eef0f5"/>
  <path d="M0,2098 C200,2000 450,1963 650,1966 C900,1970 1100,2030 1200,2102 V2390 H0 Z" fill="#f5b914"/>
  <path d="M0,2122 C250,2030 500,2000 700,2004 C950,2010 1100,2060 1200,2114 V2388 H0 Z" fill="url(#cityBlue)"/>
  <path d="M0,3210 C120,3270 300,3286 600,3286 C900,3286 1100,3276 1200,3250 V3700 H0 Z" fill="#0c3b9c"/>
</svg>

<header class="site-header">
  <div class="brand abs"><span class="brand-dot"></span>Harbor Work Agency</div>
  <nav class="main-nav abs">
    <svg viewBox="0 0 24 24"><path d="M3 11 12 3l9 8h-3v9h-5v-6h-2v6H6v-9z" fill="#f5b914"/></svg>
    <span>Candidates</span><span>Employers</span><span>Services</span><span>About Us</span><span>Vancouver Location</span><span>Contact Us</span>
  </nav>
  <a class="btn btn-yellow btn-register abs">Client Registration</a>
</header>

<section class="hero">
  <h1 class="hero-title abs">Connecting<br>Skilled Talent with<br>Leading Employers</h1>
  <a class="btn btn-yellow btn-candidates abs">For Candidates</a>
  <a class="btn btn-employers abs">For Employers</a>
</section>

<section class="solutions">
  <h2 class="section-title solutions-title abs">Our Staffing Solutions</h2>
  <svg class="abs" style="left:390px;top:900px" width="420" height="260" viewBox="0 0 420 260" aria-hidden="true">
    <ellipse cx="210" cy="130" rx="190" ry="108" fill="none" stroke="#d6deef" stroke-width="3"/>
  </svg>
  <div class="diagram-name abs">HWA</div>

  <div class="node abs" style="left:446px;top:896px"><div class="node-inner">
    <svg viewBox="0 0 32 32" fill="none" stroke="#0e2b6e" stroke-width="1.6"><path d="M4 28V14l7 4v-4l7 4V8h4v20zM24 10V5h3v23M8 22h3M14 22h3M20 22h2"/></svg>
  </div></div>
  <div class="node-label abs" style="right:772px;top:924px">Manufacturing</div>

  <div class="node abs" style="left:663px;top:893px"><div class="node-inner">
    <svg viewBox="0 0 32 32" fill="none" stroke="#0e2b6e" stroke-width="1.6"><path d="M10 28 16 4l6 24M12 20h8M13 14h6M6 28h20M16 4v24"/></svg>
  </div></div>
  <div class="node-label abs" style="left:764px;top:922px">Oil, Gas and Mining</div>

  <div class="node abs" style="left:393px;top:1030px"><div class="node-inner">
    <svg viewBox="0 0 32 32" fill="none" stroke="#0e2b6e" stroke-width="1.6"><path d="M4 12 16 5l12 7v16H4zM9 28V16h14v12M9 20h14M9 24h14"/></svg>
  </div></div>
  <div class="node-label abs" style="right:818px;top:1059px">Warehouse &amp; Logistics</div>

  <div class="node abs" style="left:725px;top:1030px"><div class="node-inner">
    <svg viewBox="0 0 32 32" fill="none" stroke="#0e2b6e" stroke-width="1.6"><circle cx="13" cy="11" r="5"/><path d="M4 27c0-5 4-9 9-9 2 0 3 .3 4 1"/><circle cx="23" cy="23" r="3"/><path d="M23 17v2M23 27v2M17 23h2M27 23h2"/></svg>
  </div></div>
  <div class="node-label abs" style="left:819px;top:1059px">Administrative</div>

  <div class="node is-active abs" style="left:559px;top:1089px"><div class="node-inner">
    <svg viewBox="0 0 32 32" fill="none" stroke="#ffffff" stroke-width="1.8"><path d="M7 16a9 9 0 0 1 18 0M5 16h22M14 8v5M18 8v5M8 28c0-4 3-7 8-7s8 3 8 7"/></svg>
  </div></div>

  <h3 class="sector-title abs">Construction &amp; Trades</h3>
  <p class="sector-text abs">Qualified tradespeople and construction workers ready to support projects of all sizes with skill and precision.</p>
  <div class="sector-link abs"><a class="link-more">Learn More ›</a></div>
</section>

<section class="about">
  <div class="about-photo abs" role="img" aria-label="Two colleagues seated on a sofa reviewing work on a laptop in a bright office"></div>
  <h2 class="about-title abs">About Harbor<br>Work Agency</h2>
  <div class="about-text abs">
    <p>Harbor Work Agency offers a complete range of staffing services to keep pace with your career or operational demands. We understand it's not only daunting but very costly in both time and money to make your business thrive in a rapidly changing environment.</p>
    <p>Our staffing and recruitment services are not just limited to finding good people. We are a Canada-wide team of capable search specialists, career counselors...</p>
  </div>
  <a class="btn btn-yellow btn-about abs">Find Out More</a>
</section>

<section class="locations">
  <h2 class="section-title locations-title abs">Our Locations</h2>
  <article class="location-card abs" style="left:134px">
    <div class="location-photo" role="img" aria-label="Aerial view of the Calgary downtown skyline and river bridges" style="background:linear-gradient(160deg,#b7c7d8 0%,#6f8aa3 45%,#7d8a5a 80%,#c99a4a 100%)"></div>
    <h3 class="location-name">Calgary Location</h3>
    <a class="link-more">View Locations ›</a>
  </article>
  <article class="location-card abs" style="left:450px">
    <div class="location-photo" role="img" aria-label="Aerial view of the Toronto skyline with its tall tower and waterfront" style="background:linear-gradient(160deg,#a9bfd6 0%,#8094a8 40%,#5b6470 75%,#3f4650 100%)"></div>
    <h3 class="location-name">Toronto Location</h3>
    <a class="link-more">View Locations ›</a>
  </article>
  <article class="location-card abs" style="left:764px">
    <div class="location-photo" role="img" aria-label="Vancouver waterfront with apartment towers, trees and beach" style="background:linear-gradient(170deg,#6ea8e6 0%,#9cc2e8 35%,#b89c78 60%,#4f6a45 85%,#2f5e7a 100%)"></div>
    <h3 class="location-name">Vancouver Location</h3>
    <a class="link-more">View Locations ›</a>
  </article>
</section>

<section class="testimonials">
  <h2 class="section-title testimonial-title abs">Hear from Our Candidates<br>and Employers</h2>
  <div class="quote-ghost abs" aria-hidden="true">“</div>
  <div class="quote-badge abs" aria-hidden="true">“</div>
  <blockquote class="quote-text abs">"We partnered with Harbor Work for our warehouse staffing needs. They provided highly qualified candidates quickly, making our hiring process effortless."</blockquote>
  <div class="stars abs" aria-label="Five stars">
    <svg viewBox="0 0 24 24"><path d="M12 2l3 7h7l-5.6 4.3 2.1 7.2L12 16.3 5.5 20.5l2.1-7.2L2 9h7z" fill="#0c3b9c"/></svg>
    <svg viewBox="0 0 24 24"><path d="M12 2l3 7h7l-5.6 4.3 2.1 7.2L12 16.3 5.5 20.5l2.1-7.2L2 9h7z" fill="#0c3b9c"/></svg>
    <svg viewBox="0 0 24 24"><path d="M12 2l3 7h7l-5.6 4.3 2.1 7.2L12 16.3 5.5 20.5l2.1-7.2L2 9h7z" fill="#0c3b9c"/></svg>
    <svg viewBox="0 0 24 24"><path d="M12 2l3 7h7l-5.6 4.3 2.1 7.2L12 16.3 5.5 20.5l2.1-7.2L2 9h7z" fill="#0c3b9c"/></svg>
    <svg viewBox="0 0 24 24"><path d="M12 2l3 7h7l-5.6 4.3 2.1 7.2L12 16.3 5.5 20.5l2.1-7.2L2 9h7z" fill="#0c3b9c"/></svg>
  </div>
  <p class="quote-author abs">— Daniel R., HR Manager</p>
  <div class="dots abs"><span></span><span></span><span></span></div>
</section>

<section class="cta-band">
  <div class="cta abs" role="img" aria-label="Faint city skyline over a warm yellow background"></div>
  <div class="cta-name abs"><span class="brand-dot"></span>Harbor Work</div>
  <p class="cta-kicker abs">Ready to Get Started?</p>
  <h2 class="cta-heading abs">Harbor Work Agency<br>offer various opportunities in the<br>different industries.</h2>
  <a class="btn btn-apply abs">Apply Here</a>
</section>

<footer class="site-footer">
  <div class="brand abs"><span class="brand-dot"></span>Harbor Work Agency</div>
  <p class="footer-tagline abs">Skilled people for growing teams</p>
  <div class="socials abs"><span></span><span></span></div>

  <div class="footer-col col-links abs">
    <h4>Quick Links</h4>
    <ul><li>Candidates</li><li>Employers</li><li>Services</li><li>About Us</li><li>Vancouver Location</li><li>Contact Us</li></ul>
  </div>
  <div class="footer-col col-contact abs">
    <h4>Contact Us</h4>
    <ul><li>Oil, Gas &amp; Mining</li><li>Administrative</li><li>Construction &amp; Trades</li><li>Warehouse &amp; Logistics</li><li>Manufacturing</li></ul>
  </div>
  <div class="footer-col col-news abs">
    <h4>Newsletter</h4>
    <p>Be the first to know about our latest products</p>
  </div>
  <div class="news-input abs">Enter you email address</div>
  <a class="btn btn-yellow btn-subscribe abs">Subscribe</a>

  <div class="bottom-bar abs">
    <span class="copy">© Harbor Work Agency Ltd. | All rights reserved 2026</span>
    <span class="legal">Terms of Use &nbsp;|&nbsp; Login</span>
  </div>
  <div class="chat-bubble abs" aria-label="Chat">
    <svg viewBox="0 0 32 32"><path d="M16 5C9 5 4 9.5 4 15c0 3 1.5 5.6 4 7.4V28l5-3.3c1 .2 2 .3 3 .3 7 0 12-4.5 12-10S23 5 16 5z" fill="#ffffff"/><circle cx="11" cy="15" r="1.6" fill="#f5b914"/><circle cx="16" cy="15" r="1.6" fill="#f5b914"/><circle cx="21" cy="15" r="1.6" fill="#f5b914"/></svg>
  </div>
</footer>

</body>
</html>
```